Harborline Talent IT Recruiting firm needs a business card design for Recruiters, Sourcers, and Account

We need business cards that allow us to change all contact info, names, titles (Recruiter, Sourcer, Account Manager, Director, CEO, etc) per person since we have three offices, in three cities, Phoenix, Austin, and Las Vegas. We do recruiting and contractors for IT positions (Developers, Architects, Software Engineers, Security Engineers, Help Desk, DBAs, PMs, Scrum Masters, etc.) Our client companies are very diverse from Crestline 250 to silicone Valley type start-ups.

So, while we what hip, techie, and quirky, it still needs to be professional. Primary color we use is blue, with silver as a secondary color.

Target Market(s)

IT, Technology

Industry/Entity Type

Business

Contact Information for Business Card

Company name: Harborline Talent, Inc.
Website: www.harborlinetalent-example.com
Logos for ProCircle, Quillo, and Roomwall

Name, Title, Office Number, Cell Number, email

Font styles to use
Serif
Sans Serif

Colors
0455a3
d5d5d5

Requirements
Nice to have
• The grey I selected below is not necessary - but, would like silver included. I included a card design (File 3: HTI early trial example.jpg) that I had started on. It's very rough, and not quite what we're looking for, but what we did like is the logo, big, maybe a bit faded, off center, goes out of frame, etc. Still looking for other ideas - you are the pros! But, just an idea of a design element we liked.

```html
<!DOCTYPE html>
<html lang="en">
<head>
<meta charset="utf-8">
<title>Harborline Talent — Business Card</title>
<link rel="stylesheet" href="https://fonts.googleapis.com/css2?family=Roboto+Condensed:wght@400;500&display=swap">
<style>
  :root {
    --backdrop: #bdb5ae;
    --card: #f4f6f5;
    --ink: #1f1f1f;
    --muted: #555555;
    --band-dark: #222222;
    --band-blue: #4a8db5;
    --brand-blue: #2c7bc8;
    --watermark: #dbe3ec;
    --on-dark: #e9e9e9;
    --icon: #3d6f9e;
  }
  * { box-sizing: border-box; margin: 0; padding: 0; }
  html, body {
    width: 1200px; height: 799px; overflow: hidden;
    background: var(--backdrop);
    font-family: "Roboto Condensed", Arial, sans-serif;
    color: var(--ink);
  }
  .stage {
    position: relative; width: 1200px; height: 799px;
    display: flex; align-items: center; justify-content: center; gap: 40px;
  }
  .card {
    position: relative; width: 540px; height: 309px;
    background: var(--card); overflow: hidden;
    box-shadow: 0 6px 18px rgba(0,0,0,.18);
  }
  .card__shapes { position: absolute; inset: 0; width: 100%; height: 100%; }

  .wordmark {
    position: absolute; color: var(--brand-blue);
    font-weight: 500; letter-spacing: .06em; text-transform: uppercase; line-height: 1;
    display: flex; align-items: center; gap: 10px; white-space: nowrap;
  }
  .wordmark__dot { width: 14px; height: 14px; border-radius: 50%; background: var(--brand-blue); flex: none; }
  .tagline {
    position: absolute; font-weight: 400; color: var(--muted); white-space: nowrap;
  }

  /* Front */
  .front .wordmark { left: 26px; top: 30px; font-size: 24px; }
  .front .tagline { left: 26px; top: 66px; font-size: 12px; }
  .contact-block {
    position: absolute; left: 22px; top: 126px; width: 232px;
    color: var(--on-dark); font-size: 10.5px; line-height: 15px;
  }
  .social { display: flex; align-items: center; gap: 7px; }
  .social__icon { width: 10px; height: 10px; border-radius: 50%; background: var(--icon); flex: none; }
  .web-block {
    position: absolute; left: 300px; top: 104px; font-size: 11.5px; line-height: 18px;
  }
  .person { position: absolute; left: 300px; top: 224px; color: #fff; }
  .person__name { font-size: 25px; font-weight: 500; line-height: 1.1; }
  .person__title { font-size: 12.5px; margin-top: 4px; }

  /* Back */
  .back .wordmark { left: 50%; top: 128px; transform: translateX(-50%); font-size: 36px; }
  .back .wordmark__dot { width: 20px; height: 20px; }
  .back .tagline { left: 0; right: 0; top: 178px; text-align: center; font-size: 14px; }
</style>
</head>
<body>
<main class="stage">

  <section class="card front" aria-label="Business card front">
    <svg class="card__shapes" viewBox="0 0 540 309" aria-hidden="true">
      <circle cx="300" cy="160" r="125" fill="var(--watermark)"/>
      <polygon points="0,118 262,118 238,236 0,236" fill="var(--band-dark)"/>
      <polygon points="284,206 540,206 540,296 266,296" fill="var(--band-blue)"/>
    </svg>

    <div class="wordmark"><span class="wordmark__dot"></span>Harborline Talent</div>
    <p class="tagline">IT talent for every build</p>

    <div class="contact-block">
      <p>Harborline Talent, Inc. 4120 E Larkspur Way, Suite 210</p>
      <p>Phoenix, AZ 85099, USA</p>
      <p>Phone: 555 014-2730, Fax: 555 014-2731</p>
      <p class="social"><span class="social__icon"></span>Roomwall name</p>
      <p class="social"><span class="social__icon"></span>@marisoldenholmHT</p>
      <p class="social"><span class="social__icon"></span>ProCircle name</p>
    </div>

    <div class="web-block">
      <p>Website: www.harborlinetalent-example.com</p>
      <p>Email: marisol@harborlinetalent-example.com</p>
    </div>

    <div class="person">
      <p class="person__name">Marisol Denholm</p>
      <p class="person__title">First Touch Embassador</p>
    </div>
  </section>

  <section class="card back" aria-label="Business card back">
    <div class="wordmark"><span class="wordmark__dot"></span>Harborline Talent</div>
    <p class="tagline">IT talent for every build</p>
  </section>

</main>
</body>
</html>
```